App-Design für IT-Sicherheitsfirma
Zielgruppe
Wir sind eine IT-Sicherheitsfirma und suchen ein funktionelles und schlankes App Design.
Unsere Nutzer sind Mitarbeiter von international agierenden Konzernen. Die Zielgruppe sind international agierende Konzerne.
Die App gibt die Möglichkeit zu einem sehr sicheren Login auf Großrechner (Mainframes) via Handy oder Webinterface. Vereinfacht gesagt ist sie ein Login-Tool, Schlüssel oder Authenticator.
Aufgabenstellung
Die App soll übersichtlich, sicher, modern, schlicht und smart aussehen. Schön aber kein muss wäre die Verwendung von Elementen aus 'wirbel/gestalt' da wir die App auf dieser Plattform programmieren wollen.
https://gestaltkern.io/design/gestalt-theming/overview.html#gestalt-theming
https://wirbel.dev/docs/development/ui/widgets/gestalt

```html
<!DOCTYPE html>
<html lang="de">
<head>
<meta charset="utf-8">
<title>Harbor Pass – App Screens</title>
<link href="https://fonts.googleapis.com/css2?family=Roboto:wght@400;500;700&display=swap" rel="stylesheet">
<style>
:root{
  --stage:#b3b3b2;
  --paper:#f4f4f4;
  --card:#ffffff;
  --ink:#1d1d1d;
  --muted:#8a8a8a;
  --accent:#c8102e;
  --accent-soft:#fbe3e7;
  --ok:#1f9e2c;
  --bar:#000000;
  --tab:#f2f2f2;
  --well:#ebebeb;
}
*{box-sizing:border-box;margin:0;padding:0}
html,body{width:1200px;height:4473px;overflow:hidden}
body{background:var(--stage);font-family:"Roboto",sans-serif;color:var(--ink);position:relative}

.screen{position:absolute;overflow:hidden;background:linear-gradient(160deg,#ffffff 0%,#f1f1f1 45%,#e9e9e9 100%)}
.screen.well{background:linear-gradient(180deg,#f6f6f6 0%,#efefef 22%,var(--well) 32%,var(--well) 100%)}

.status{position:absolute;top:8px;right:14px;display:flex;gap:6px;align-items:center}
.status i{display:block;width:8px;height:8px;background:#9a9a9a}
.status i:nth-child(2){border-radius:50%}
.status i:nth-child(3){width:0;height:0;background:none;border-left:5px solid transparent;border-right:5px solid transparent;border-top:8px solid #9a9a9a}

.brand-line{position:absolute;top:38px;left:22px;font-size:18px;font-weight:500}
.gear{position:absolute;top:36px;right:18px;width:20px;height:20px}
.title{position:absolute;top:84px;left:22px;font-size:29px;line-height:33px;font-weight:700;letter-spacing:-.2px}

.list{position:absolute;top:175px;left:22px;right:22px;bottom:92px;overflow:hidden;display:flex;flex-direction:column;gap:16px}
.list.tight{left:12px;right:12px}
.list.frames{gap:19px}

.req{background:var(--card);height:38px;flex:none;display:flex;align-items:center;padding:0 10px 0 14px;box-shadow:0 1px 2px rgba(0,0,0,.12)}
.req .mail{font-size:13px;font-weight:700;flex:1;white-space:nowrap;overflow:hidden;text-overflow:ellipsis}
.req.open{height:98px;flex-direction:column;align-items:stretch;padding:10px 10px 10px 14px;gap:8px}
.req.open .row{display:flex;align-items:center}
.req.open .icons{display:flex;gap:6px}
.date{font-size:12px;color:var(--muted)}

.req.compact{height:59px;padding:0 10px 0 12px}
.req.compact .txt{flex:1;min-width:0}
.req.compact .date{font-size:11px;margin-top:3px}
.req.compact .icons{display:flex;gap:6px;align-items:center}

.ico{width:18px;height:18px;flex:none}
.ico.sm{width:16px;height:16px}

.frame{background:var(--card);height:70px;flex:none;display:flex;align-items:flex-start;padding:14px 12px 0 18px;box-shadow:0 1px 2px rgba(0,0,0,.12)}
.proto{width:52px;font-size:13px;font-weight:700}
.proto.badge{width:36px;height:34px;margin-right:16px;margin-top:2px;background:var(--accent-soft);color:var(--accent);display:flex;align-items:center;justify-content:center;border-radius:2px}
.frame .txt{flex:1}
.frame .name{font-size:13px}
.frame .host{font-size:13px;color:var(--muted);margin-top:7px}

.tabbar{position:absolute;left:0;right:0;bottom:41px;height:51px;background:var(--tab);display:flex}
.tab{flex:1;display:flex;flex-direction:column;align-items:center;justify-content:center;gap:3px;font-size:10px;color:var(--muted)}
.tab svg{width:18px;height:18px}
.tab.active{color:var(--accent)}
.navbar{position:absolute;left:0;right:0;bottom:0;height:41px;background:var(--bar);display:flex;justify-content:space-around;align-items:center;padding:0 50px}
.navbar svg{width:16px;height:16px}

.splash{display:flex;align-items:center;justify-content:center}
.splash .art{position:absolute;inset:0}
.splash .word{position:relative;font-size:34px;font-weight:700;letter-spacing:1px;margin-top:-80px;display:flex;align-items:center;gap:8px}
.splash .word span{display:block;width:12px;height:12px;background:var(--accent)}
</style>
</head>
<body>

<svg width="0" height="0" style="position:absolute" aria-hidden="true">
  <symbol id="i-ok" viewBox="0 0 20 20"><circle cx="10" cy="10" r="9" fill="#1f9e2c"/><path d="M5.5 10.3l3 3 6-6.3" stroke="#fff" stroke-width="2.2" fill="none" stroke-linecap="round" stroke-linejoin="round"/></symbol>
  <symbol id="i-phone" viewBox="0 0 20 20"><rect x="5.5" y="2" width="9" height="16" rx="1.5" fill="none" stroke="#1d1d1d" stroke-width="2"/></symbol>
  <symbol id="i-chip" viewBox="0 0 20 20"><circle cx="10" cy="10" r="6" fill="none" stroke="#1d1d1d" stroke-width="1.8"/><path d="M10 1v3M10 16v3M1 10h3M16 10h3M7 10h6M10 7v6" stroke="#1d1d1d" stroke-width="1.6"/></symbol>
  <symbol id="i-print" viewBox="0 0 20 20"><g fill="none" stroke="#a6a6a6" stroke-width="1.4"><circle cx="10" cy="10" r="8"/><circle cx="10" cy="10" r="5.5"/><circle cx="10" cy="10" r="3"/><path d="M10 9v3"/></g></symbol>
  <symbol id="i-down" viewBox="0 0 20 20"><path d="M5 8l5 5 5-5" fill="none" stroke="#1d1d1d" stroke-width="2"/></symbol>
  <symbol id="i-up" viewBox="0 0 20 20"><path d="M5 12l5-5 5 5" fill="none" stroke="#1d1d1d" stroke-width="2"/></symbol>
  <symbol id="i-gear" viewBox="0 0 24 24"><path fill="#1d1d1d" d="M19.4 13a7.5 7.5 0 000-2l2.1-1.6-2-3.5-2.5 1a7 7 0 00-1.7-1L14.9 3h-4l-.4 2.9a7 7 0 00-1.7 1l-2.5-1-2 3.5L6.4 11a7.5 7.5 0 000 2l-2.1 1.6 2 3.5 2.5-1a7 7 0 001.7 1l.4 2.9h4l.4-2.9a7 7 0 001.7-1l2.5 1 2-3.5zM12.9 15.5a3.5 3.5 0 110-7 3.5 3.5 0 010 7z"/></symbol>
  <symbol id="i-login" viewBox="0 0 20 20"><g fill="none" stroke="#1d1d1d" stroke-width="1.8"><path d="M11 3h6v14h-6"/><path d="M3 10h10M9.5 6.5L13 10l-3.5 3.5"/></g></symbol>
  <symbol id="i-terminal" viewBox="0 0 20 20"><rect x="3" y="2" width="14" height="16" rx="1.5" fill="currentColor"/><path d="M6 7h8M6 10h8M6 13h5" stroke="#fff" stroke-width="1.5"/></symbol>
  <symbol id="i-history" viewBox="0 0 20 20"><g fill="none" stroke="currentColor" stroke-width="1.7"><path d="M4 10a6.5 6.5 0 106.5-6.5A6.5 6.5 0 004.6 7.2"/><path d="M2.5 5.5l2 2 2.2-1.8"/><path d="M10.5 6.5V10l2.5 1.8"/></g></symbol>
  <symbol id="n-back" viewBox="0 0 16 16"><path d="M12 2L3 8l9 6z" fill="none" stroke="#fff" stroke-width="1.6"/></symbol>
  <symbol id="n-home" viewBox="0 0 16 16"><circle cx="8" cy="8" r="6" fill="none" stroke="#fff" stroke-width="1.6"/></symbol>
  <symbol id="n-apps" viewBox="0 0 16 16"><rect x="2.5" y="2.5" width="11" height="11" fill="none" stroke="#fff" stroke-width="1.6"/></symbol>
</svg>

<!-- Splash dark -->
<section class="screen splash" style="left:165px;top:96px;width:370px;height:779px;background:#000">
  <div class="art" role="img" aria-label="Dunkles facettiertes Polygonmuster als Hintergrund" style="background:linear-gradient(160deg,#3a3a3a 0%,#1c1c1c 40%,#080808 100%)"></div>
  <div class="status"><i></i><i></i><i></i></div>
  <div class="word" style="color:#fff">Velqon<span></span></div>
  <nav class="navbar"><svg><use href="#n-back"/></svg><svg><use href="#n-home"/></svg><svg><use href="#n-apps"/></svg></nav>
</section>

<!-- Splash light -->
<section class="screen splash" style="left:660px;top:96px;width:368px;height:776px">
  <div class="art" role="img" aria-label="Helles facettiertes Polygonmuster als Hintergrund" style="background:linear-gradient(160deg,#e6e6e6 0%,#f7f7f7 45%,#ffffff 100%)"></div>
  <div class="status"><i></i><i></i><i></i></div>
  <div class="word" style="color:#111">Velqon<span></span></div>
  <nav class="navbar"><svg><use href="#n-back"/></svg><svg><use href="#n-home"/></svg><svg><use href="#n-apps"/></svg></nav>
</section>

<!-- Requests expandable, tall -->
<section class="screen" style="left:168px;top:969px;width:372px;height:783px">
  <div class="status"><i></i><i></i><i></i></div>
  <div class="brand-line">Harbor Pass</div>
  <svg class="gear"><use href="#i-gear"/></svg>
  <h1 class="title">Authentication<br>Requests</h1>
  <div class="list">
    <div class="req open">
      <div class="row"><span class="mail">Maxmustermann@demo.test</span><svg class="ico"><use href="#i-ok"/></svg><svg class="ico" style="margin-left:18px"><use href="#i-up"/></svg></div>
      <div class="icons"><svg class="ico sm"><use href="#i-phone"/></svg><svg class="ico sm"><use href="#i-chip"/></svg><svg class="ico sm"><use href="#i-print"/></svg></div>
      <div class="date">7/19/2021 09:22:16</div>
    </div>
    <div class="req"><span class="mail">Lena.Schmitz@harborpass.test</span><svg class="ico"><use href="#i-ok"/></svg><svg class="ico" style="margin-left:18px"><use href="#i-down"/></svg></div>
    <div class="req"><span class="mail">Maxmustermann@demo.test</span><svg class="ico"><use href="#i-ok"/></svg><svg class="ico" style="margin-left:18px"><use href="#i-down"/></svg></div>
    <div class="req"><span class="mail">Maxmustermann@demo.test</span><svg class="ico"><use href="#i-ok"/></svg><svg class="ico" style="margin-left:18px"><use href="#i-down"/></svg></div>
    <div class="req"><span class="mail">Maxmustermann@demo.test</span><svg class="ico"><use href="#i-ok"/></svg><svg class="ico" style="margin-left:18px"><use href="#i-down"/></svg></div>
    <div class="req"><span class="mail">Maxmustermann@demo.test</span><svg class="ico"><use href="#i-ok"/></svg><svg class="ico" style="margin-left:18px"><use href="#i-down"/></svg></div>
    <div class="req"><span class="mail">Maxmustermann@demo.test</span><svg class="ico"><use href="#i-ok"/></svg><svg class="ico" style="margin-left:18px"><use href="#i-down"/></svg></div>
    <div class="req"><span class="mail">Maxmustermann@demo.test</span><svg class="ico"><use href="#i-ok"/></svg><svg class="ico" style="margin-left:18px"><use href="#i-down"/></svg></div>
    <div class="req"><span class="mail">Maxmustermann@demo.test</span><svg class="ico"><use href="#i-ok"/></svg><svg class="ico" style="margin-left:18px"><use href="#i-down"/></svg></div>
  </div>
  <div class="tabbar"><div class="tab"><svg><use href="#i-terminal"/></svg>Terminal</div><div class="tab active"><svg><use href="#i-history"/></svg>Logins</div></div>
  <nav class="navbar"><svg><use href="#n-back"/></svg><svg><use href="#n-home"/></svg><svg><use href="#n-apps"/></svg></nav>
</section>

<!-- Requests expandable, short -->
<section class="screen" style="left:660px;top:969px;width:337px;height:601px">
  <div class="status"><i></i><i></i><i></i></div>
  <div class="brand-line" style="left:14px">Harbor Pass</div>
  <svg class="gear"><use href="#i-gear"/></svg>
  <h1 class="title" style="left:14px">Authentication<br>Requests</h1>
  <div class="list" style="left:12px;right:12px">
    <div class="req open">
      <div class="row"><span class="mail">Maxmustermann@demo.test</span><svg class="ico"><use href="#i-ok"/></svg><svg class="ico" style="margin-left:8px"><use href="#i-up"/></svg></div>
      <div class="icons"><svg class="ico sm"><use href="#i-phone"/></svg><svg class="ico sm"><use href="#i-chip"/></svg><svg class="ico sm"><use href="#i-print"/></svg></div>
      <div class="date">7/19/2021 09:22:16</div>
    </div>
    <div class="req"><span class="mail">Lena.Schmitz@harborpass.test</span><svg class="ico"><use href="#i-ok"/></svg><svg class="ico" style="margin-left:8px"><use href="#i-down"/></svg></div>
    <div class="req"><span class="mail">Maxmustermann@demo.test</span><svg class="ico"><use href="#i-ok"/></svg><svg class="ico" style="margin-left:8px"><use href="#i-down"/></svg></div>
    <div class="req"><span class="mail">Maxmustermann@demo.test</span><svg class="ico"><use href="#i-ok"/></svg><svg class="ico" style="margin-left:8px"><use href="#i-down"/></svg></div>
    <div class="req"><span class="mail">Maxmustermann@demo.test</span><svg class="ico"><use href="#i-ok"/></svg><svg class="ico" style="margin-left:8px"><use href="#i-down"/></svg></div>
  </div>
  <div class="tabbar"><div class="tab active"><svg><use href="#i-terminal"/></svg>Terminal</div><div class="tab"><svg><use href="#i-history"/></svg>Logins</div></div>
  <nav class="navbar"><svg><use href="#n-back"/></svg><svg><use href="#n-home"/></svg><svg><use href="#n-apps"/></svg></nav>
</section>

<!-- Requests compact, tall -->
<section class="screen" style="left:168px;top:1846px;width:372px;height:781px">
  <div class="status"><i></i><i></i><i></i></div>
  <div class="brand-line">Harbor Pass</div>
  <svg class="gear"><use href="#i-gear"/></svg>
  <h1 class="title">Authentication<br>Requests</h1>
  <div class="list tight">
    <div class="req compact"><div class="txt"><div class="mail">Maxmustermann@demo.test</div><div class="date">7/19/2021 09:22:16</div></div><div class="icons"><svg class="ico"><use href="#i-ok"/></svg><svg class="ico sm"><use href="#i-phone"/></svg><svg class="ico sm"><use href="#i-chip"/></svg><svg class="ico sm"><use href="#i-print"/></svg></div></div>
    <div class="req compact"><div class="txt"><div class="mail">Maxmustermann@demo.test</div><div class="date">7/19/2021 09:22:16</div></div><div class="icons"><svg class="ico"><use href="#i-ok"/></svg><svg class="ico sm"><use href="#i-phone"/></svg><svg class="ico sm"><use href="#i-chip"/></svg><svg class="ico sm"><use href="#i-print"/></svg></div></div>
    <div class="req compact"><div class="txt"><div class="mail">Maxmustermann@demo.test</div><div class="date">7/19/2021 09:22:16</div></div><div class="icons"><svg class="ico"><use href="#i-ok"/></svg><svg class="ico sm"><use href="#i-phone"/></svg><svg class="ico sm"><use href="#i-chip"/></svg><svg class="ico sm"><use href="#i-print"/></svg></div></div>
    <div class="req compact"><div class="txt"><div class="mail">Maxmustermann@demo.test</div><div class="date">7/19/2021 09:22:16</div></div><div class="icons"><svg class="ico"><use href="#i-ok"/></svg><svg class="ico sm"><use href="#i-phone"/></svg><svg class="ico sm"><use href="#i-chip"/></svg><svg class="ico sm"><use href="#i-print"/></svg></div></div>
    <div class="req compact"><div class="txt"><div class="mail">Maxmustermann@demo.test</div><div class="date">7/19/2021 09:22:16</div></div><div class="icons"><svg class="ico"><use href="#i-ok"/></svg><svg class="ico sm"><use href="#i-phone"/></svg><svg class="ico sm"><use href="#i-chip"/></svg><svg class="ico sm"><use href="#i-print"/></svg></div></div>
    <div class="req compact"><div class="txt"><div class="mail">Maxmustermann@demo.test</div><div class="date">7/19/2021 09:22:16</div></div><div class="icons"><svg class="ico"><use href="#i-ok"/></svg><svg class="ico sm"><use href="#i-phone"/></svg><svg class="ico sm"><use href="#i-chip"/></svg><svg class="ico sm"><use href="#i-print"/></svg></div></div>
    <div class="req compact"><div class="txt"><div class="mail">Maxmustermann@demo.test</div><div class="date">7/19/2021 09:22:16</div></div><div class="icons"><svg class="ico"><use href="#i-ok"/></svg><svg class="ico sm"><use href="#i-phone"/></svg><svg class="ico sm"><use href="#i-chip"/></svg><svg class="ico sm"><use href="#i-print"/></svg></div></div>
  </div>
  <div class="tabbar"><div class="tab"><svg><use href="#i-terminal"/></svg>Terminal</div><div class="tab active"><svg><use href="#i-history"/></svg>Logins</div></div>
  <nav class="navbar"><svg><use href="#n-back"/></svg><svg><use href="#n-home"/></svg><svg><use href="#n-apps"/></svg></nav>
</section>

<!-- Requests compact, short -->
<section class="screen" style="left:660px;top:1846px;width:337px;height:601px">
  <div class="status"><i></i><i></i><i></i></div>
  <div class="brand-line" style="left:14px">Harbor Pass</div>
  <svg class="gear"><use href="#i-gear"/></svg>
  <h1 class="title" style="left:14px">Authentication<br>Requests</h1>
  <div class="list tight">
    <div class="req compact"><div class="txt"><div class="mail">Maxmustermann@demo.test</div><div class="date">7/19/2021 09:22:16</div></div><div class="icons"><svg class="ico"><use href="#i-ok"/></svg><svg class="ico sm"><use href="#i-phone"/></svg><svg class="ico sm"><use href="#i-chip"/></svg><svg class="ico sm"><use href="#i-print"/></svg></div></div>
    <div class="req compact"><div class="txt"><div class="mail">Maxmustermann@demo.test</div><div class="date">7/19/2021 09:22:16</div></div><div class="icons"><svg class="ico"><use href="#i-ok"/></svg><svg class="ico sm"><use href="#i-phone"/></svg><svg class="ico sm"><use href="#i-chip"/></svg><svg class="ico sm"><use href="#i-print"/></svg></div></div>
    <div class="req compact"><div class="txt"><div class="mail">Maxmustermann@demo.test</div><div class="date">7/19/2021 09:22:16</div></div><div class="icons"><svg class="ico"><use href="#i-ok"/></svg><svg class="ico sm"><use href="#i-phone"/></svg><svg class="ico sm"><use href="#i-chip"/></svg><svg class="ico sm"><use href="#i-print"/></svg></div></div>
    <div class="req compact"><div class="txt"><div class="mail">Maxmustermann@demo.test</div><div class="date">7/19/2021 09:22:16</div></div><div class="icons"><svg class="ico"><use href="#i-ok"/></svg><svg class="ico sm"><use href="#i-phone"/></svg><svg class="ico sm"><use href="#i-chip"/></svg><svg class="ico sm"><use href="#i-print"/></svg></div></div>
    <div class="req compact"><div class="txt"><div class="mail">Maxmustermann@demo.test</div><div class="date">7/19/2021 09:22:16</div></div><div class="icons"><svg class="ico"><use href="#i-ok"/></svg><svg class="ico sm"><use href="#i-phone"/></svg><svg class="ico sm"><use href="#i-chip"/></svg><svg class="ico sm"><use href="#i-print"/></svg></div></div>
  </div>
  <div class="tabbar"><div class="tab active"><svg><use href="#i-terminal"/></svg>Terminal</div><div class="tab"><svg><use href="#i-history"/></svg>Logins</div></div>
  <nav class="navbar"><svg><use href="#n-back"/></svg><svg><use href="#n-home"/></svg><svg><use href="#n-apps"/></svg></nav>
</section>

<!-- Mainframe list, tall -->
<section class="screen well" style="left:168px;top:2723px;width:370px;height:774px">
  <div class="status"><i></i><i></i><i></i></div>
  <div class="brand-line">Harbor Pass</div>
  <svg class="gear"><use href="#i-gear"/></svg>
  <h1 class="title">Wähle einen<br>Mainframe aus</h1>
  <div class="list frames">
    <div class="frame"><div class="proto">tso</div><div class="txt"><div class="name">Velqon Demo</div><div class="host">Mainframe-dev.velqon.test</div></div><svg class="ico"><use href="#i-login"/></svg></div>
    <div class="frame"><div class="proto">tso</div><div class="txt"><div class="name">Velqon Demo</div><div class="host">Mainframe-dev.velqon.test</div></div><svg class="ico"><use href="#i-login"/></svg></div>
    <div class="frame"><div class="proto">tso</div><div class="txt"><div class="name">Velqon Demo</div><div class="host">Mainframe-dev.velqon.test</div></div><svg class="ico"><use href="#i-login"/></svg></div>
  </div>
  <div class="tabbar"><div class="tab active"><svg><use href="#i-terminal"/></svg>Terminal</div><div class="tab"><svg><use href="#i-history"/></svg>Logins</div></div>
  <nav class="navbar"><svg><use href="#n-back"/></svg><svg><use href="#n-home"/></svg><svg><use href="#n-apps"/></svg></nav>
</section>

<!-- Mainframe list, short -->
<section class="screen well" style="left:662px;top:2723px;width:335px;height:594px">
  <div class="status"><i></i><i></i><i></i></div>
  <div class="brand-line" style="left:14px">Harbor Pass</div>
  <svg class="gear"><use href="#i-gear"/></svg>
  <h1 class="title" style="left:14px">Wähle einen<br>Mainframe aus</h1>
  <div class="list frames" style="left:14px;right:14px">
    <div class="frame"><div class="proto">tso</div><div class="txt"><div class="name">Velqon Demo</div><div class="host">Mainframe-dev.velqon.test</div></div><svg class="ico"><use href="#i-login"/></svg></div>
    <div class="frame"><div class="proto">tso</div><div class="txt"><div class="name">Velqon Demo</div><div class="host">Mainframe-dev.velqon.test</div></div><svg class="ico"><use href="#i-login"/></svg></div>
    <div class="frame"><div class="proto">tso</div><div class="txt"><div class="name">Velqon Demo</div><div class="host">Mainframe-dev.velqon.test</div></div><svg class="ico"><use href="#i-login"/></svg></div>
  </div>
  <div class="tabbar"><div class="tab active"><svg><use href="#i-terminal"/></svg>Terminal</div><div class="tab"><svg><use href="#i-history"/></svg>Logins</div></div>
  <nav class="navbar"><svg><use href="#n-back"/></svg><svg><use href="#n-home"/></svg><svg><use href="#n-apps"/></svg></nav>
</section>

<!-- Mainframe list with protocol badges -->
<section class="screen well" style="left:168px;top:3593px;width:370px;height:776px">
  <div class="status"><i></i><i></i><i></i></div>
  <div class="brand-line">Harbor Pass</div>
  <svg class="gear"><use href="#i-gear"/></svg>
  <h1 class="title">Wähle einen<br>Mainframe aus</h1>
  <div class="list frames">
    <div class="frame" style="padding-left:14px"><div class="proto badge">tso</div><div class="txt"><div class="name">Velqon Demo</div><div class="host">Mainframe-dev.velqon.test</div></div><svg class="ico"><use href="#i-login"/></svg></div>
    <div class="frame" style="padding-left:14px"><div class="proto badge">rfca</div><div class="txt"><div class="name">Velqon Demo</div><div class="host">Mainframe-dev.velqon.test</div></div><svg class="ico"><use href="#i-login"/></svg></div>
    <div class="frame" style="padding-left:14px"><div class="proto badge">tso</div><div class="txt"><div class="name">Velqon Demo</div><div class="host">Mainframe-dev.velqon.test</div></div><svg class="ico"><use href="#i-login"/></svg></div>
  </div>
  <div class="tabbar"><div class="tab active"><svg><use href="#i-terminal"/></svg>Terminal</div><div class="tab"><svg><use href="#i-history"/></svg>Logins</div></div>
  <nav class="navbar"><svg><use href="#n-back"/></svg><svg><use href="#n-home"/></svg><svg><use href="#n-apps"/></svg></nav>
</section>

</body>
</html>
```